Plakat-Design für Frauenfitnessstudio
Zielgruppe
Frauenfitnessstudio
Aufgabenstellung
Wir benötigen eine Außenplane die an der eingezeichneten Postion befestigt werden soll (Anhang 'Außenansicht').
Auf der Plane soll mindestens folgender Inhalt dargestellt werden:
- Logo
- Website 'morvenhalle-augsburg.de'
- Trelvano-Logo
- Pixomerat-Logo
Die Plane soll ab einer Reichweite von ca. 50 Metern erkennbar sein.
Die Maße betragen 480x280 cm.

```html
<!DOCTYPE html>
<html lang="de">
<head>
<meta charset="utf-8">
<title>Morvenhalle Augsburg – Außenplane</title>
<link href="https://fonts.googleapis.com/css2?family=Arimo:wght@400;700&display=swap" rel="stylesheet">
<style>
  :root {
    --backdrop: #d6d6d6;
    --paper: #ffffff;
    --magenta: #f0149b;
    --brand-orange: #f4a40c;
    --offer-yellow: #f2c21a;
    --offer-pink: #e8308a;
    --headline-yellow: #e8f500;
    --text-white: #ffffff;
    --purple-light: #ee6fe0;
    --purple-dark: #923a88;
    --square-blue: #27589e;
    --square-orange: #e9573f;
    --photo-cream: #f5ece4;
    --photo-peach: #f2c9a4;
    --photo-yellow: #f0c060;
    --photo-pink: #eeb0d2;
  }
  * { margin: 0; padding: 0; box-sizing: border-box; }
  html, body {
    width: 1200px; height: 675px; overflow: hidden;
    background: var(--backdrop);
    font-family: "Arimo", Arial, sans-serif;
  }
  .banner {
    position: absolute; left: 30px; top: 5px;
    width: 1140px; height: 665px;
    background: var(--paper);
    overflow: hidden;
  }
  .hero-photo {
    position: absolute; left: 330px; top: 0;
    width: 600px; height: 470px;
    background: linear-gradient(90deg,
      var(--photo-cream) 0%,
      var(--photo-pink) 30%,
      var(--photo-peach) 45%,
      var(--photo-yellow) 58%,
      var(--photo-peach) 68%,
      var(--photo-pink) 82%,
      var(--photo-cream) 100%);
    -webkit-mask-image: linear-gradient(90deg, transparent 0%, #000 30%, #000 92%, transparent 100%);
    mask-image: linear-gradient(90deg, transparent 0%, #000 30%, #000 92%, transparent 100%);
  }
  .brand-name {
    position: absolute; left: 30px; top: 112px;
    font-size: 66px; font-weight: 700; color: var(--brand-orange);
  }
  .follow {
    position: absolute; left: 927px; top: 16px;
    font-size: 47px; font-weight: 700; line-height: 46px;
    color: var(--magenta);
  }
  .socials {
    position: absolute; left: 928px; top: 138px;
    display: flex; flex-direction: column; gap: 16px;
  }
  .social {
    display: flex; align-items: center; gap: 10px;
    font-size: 26px; font-weight: 700; color: var(--magenta);
  }
  .social-square { width: 28px; height: 28px; }
  .social-square.trelvano { background: var(--square-blue); }
  .social-square.pixomerat { background: var(--square-orange); }
  .wave { position: absolute; left: 0; top: 0; width: 1140px; height: 665px; }
  .offer {
    position: absolute; left: 925px; top: 238px;
    width: 194px; height: 194px; border-radius: 50%;
    background: var(--paper);
    border: 4px solid var(--offer-yellow);
    display: flex; flex-direction: column; align-items: center; justify-content: center;
    gap: 4px; text-align: center;
  }
  .offer-claim { font-size: 14px; font-weight: 700; color: var(--offer-pink); }
  .offer-title { font-size: 30px; font-weight: 700; color: var(--offer-yellow); }
  .offer-price { font-size: 16px; font-weight: 700; color: var(--offer-pink); }
  .tagline {
    position: absolute; left: 24px; top: 456px;
    font-size: 54px; font-weight: 700; color: var(--text-white);
    white-space: nowrap;
  }
  .welcome {
    position: absolute; left: 26px; top: 520px;
    font-size: 66px; font-weight: 700; color: var(--headline-yellow);
    white-space: nowrap;
  }
  .contact {
    position: absolute; left: 28px; top: 592px;
    font-size: 47px; font-weight: 700; color: var(--text-white);
    white-space: nowrap;
  }
</style>
</head>
<body>
  <main class="banner">
    <div class="hero-photo" role="img" aria-label="Foto einer lächelnden Frau im gelben Sporttop mit Kurzhantel im hellen Fitnessstudio"></div>

    <div class="brand-name">Morvenhalle</div>

    <div class="follow">Folge<br>uns auf</div>
    <div class="socials">
      <div class="social"><span class="social-square trelvano"></span>Trelvano</div>
      <div class="social"><span class="social-square pixomerat"></span>Pixomerat</div>
    </div>

    <svg class="wave" viewBox="0 0 1140 665" aria-hidden="true">
      <defs>
        <linearGradient id="bandGradient" x1="0" y1="0" x2="1" y2="0">
          <stop offset="0" stop-color="#ee6fe0"/>
          <stop offset="0.3" stop-color="#923a88"/>
          <stop offset="0.65" stop-color="#ee6fe0"/>
          <stop offset="1" stop-color="#923a88"/>
        </linearGradient>
      </defs>
      <path d="M0 428 C 320 452 820 418 1140 272 L1140 665 L0 665 Z" fill="url(#bandGradient)"/>
    </svg>

    <div class="offer">
      <span class="offer-claim">WIR MACHEN SIE FIT!</span>
      <span class="offer-title">TRAINING</span>
      <span class="offer-price">ab 29,90 €</span>
    </div>

    <div class="tagline">Dein Morvenhalle in Augsburg.</div>
    <div class="welcome">Wir freuen uns auf Dich!</div>
    <div class="contact">morvenhalle-augsburg.de • Tel.:0821-46 27 15</div>
  </main>
</body>
</html>
```